Kettle Ledger Business Card design

We need a stand out business card design for Accounting practice based in Australia specialising in pubs, clubs and hotels. We help venues maximise margins, create time and manage cashflow. One club we have been working with for the last 6 months has increased revenue by 3% and margin by 5% in this time frame. We have a back office outsourced system that costs less than having a full time employee and also allows the venues the added benefit of:<br/>-using the office space to become a revenue generating opportunity. <br/>-a complete system to enhance governance, accountability and efficiency within their operation<br/>-52 weeks cover so no hassle to cover annual/sick .. leave<br/><br/>We would like to see designs that use the colours of our logo (green & blue).
Target Market(s)
Australian Pubs, Clubs & Hotels abookkeeping, accounting and tax services
Industry/Entity Type
Accountant
Contact Information for Business Card
Miriam Oakley CPA
Principal
Accountant Tax Agent
Miriam@KettleLedger-example.com.au
0418693142
www.kettleledger-example.com.au
Accounting / Payroll / Tax / SMSF / Technology
Colors
Designer to choose colors to be used in the design.
Look and feel
Each slider illustrates characteristics of the customer's brand and the style your logo design should communicate.

```html
<!DOCTYPE html>
<html lang="en">
<head>
<meta charset="utf-8">
<title>Kettle Ledger – Business Card</title>
<link href="https://fonts.googleapis.com/css2?family=Lato:ital,wght@0,400;0,700;0,900;1,400;1,900&display=swap" rel="stylesheet">
<style>
  :root {
    --brand-blue: #233f98;
    --brand-blue-pattern: #2a4aa6;
    --brand-green: #1b7a3a;
    --ink-grey: #444a55;
    --card-white: #ffffff;
    --stage: #e9eaec;
    --rule-green: #7fb892;
  }
  * { margin: 0; padding: 0; box-sizing: border-box; }
  html, body { width: 1200px; height: 878px; overflow: hidden; }
  body {
    background: var(--stage);
    font-family: "Lato", sans-serif;
    display: flex;
    flex-direction: column;
    align-items: center;
    justify-content: center;
    gap: 40px;
  }
  .card {
    position: relative;
    width: 660px;
    height: 378px;
    overflow: hidden;
    box-shadow: 0 6px 18px rgba(0,0,0,0.18);
  }

  /* Back */
  .card-back { background: var(--brand-blue); }
  .back-pattern {
    position: absolute; inset: 0;
    background: linear-gradient(135deg, var(--brand-blue) 0%, var(--brand-blue-pattern) 50%, var(--brand-blue) 100%);
  }
  .back-brand {
    position: absolute;
    right: 48px; top: 150px;
    display: flex; align-items: center; gap: 12px;
    color: var(--card-white);
    font-weight: 900;
    font-size: 34px;
    letter-spacing: 0.5px;
  }
  .brand-dot {
    width: 30px; height: 30px; border-radius: 50%;
    border: 3px solid currentColor;
  }

  /* Front */
  .card-front { background: var(--card-white); }
  .holder {
    position: absolute; left: 40px; top: 34px;
  }
  .holder-name {
    color: var(--brand-blue);
    font-weight: 900; font-style: italic;
    font-size: 30px; line-height: 1.1;
  }
  .holder-role {
    color: var(--ink-grey);
    font-style: italic;
    font-size: 19px; line-height: 1.25;
    margin-top: 2px;
  }
  .front-brand {
    position: absolute; right: 44px; top: 150px;
    display: flex; align-items: center; gap: 14px;
    color: var(--brand-blue);
    font-weight: 900; font-size: 38px;
  }
  .front-brand .brand-dot { width: 36px; height: 36px; border-color: var(--brand-green); }
  .contact-list {
    position: absolute; left: 40px; top: 222px;
    list-style: none;
  }
  .contact-list li {
    display: flex; align-items: center; gap: 12px;
    color: var(--ink-grey);
    font-style: italic; font-size: 19px; line-height: 1.3;
  }
  .contact-list svg { width: 16px; height: 16px; flex: none; }
  .services {
    position: absolute; left: 40px; top: 312px;
    color: var(--brand-green);
    font-style: italic; font-size: 21px;
    word-spacing: 3px;
  }
  .services-rule {
    position: absolute; left: 40px; right: 40px; top: 343px;
    height: 1px; background: var(--rule-green);
  }
  .footer-band {
    position: absolute; left: 0; right: 0; bottom: 0; height: 18px;
    display: flex;
  }
  .footer-band .band-green { width: 40px; background: var(--brand-green); height: 12px; margin-top: 0; }
  .footer-band .band-blue { flex: 1; background: var(--brand-blue); margin-left: 6px; margin-top: 4px; }
</style>
</head>
<body>

  <section class="card card-back">
    <div class="back-pattern" role="img" aria-label="Repeating pattern of outlined hop cones in a lighter blue"></div>
    <div class="back-brand"><span class="brand-dot"></span>Kettle Ledger</div>
  </section>

  <section class="card card-front">
    <div class="holder">
      <div class="holder-name">Miriam Oakley CPA</div>
      <div class="holder-role">Principal<br>Accountant Tax Agent</div>
    </div>

    <div class="front-brand"><span class="brand-dot"></span>Kettle Ledger</div>

    <ul class="contact-list">
      <li>
        <svg viewBox="0 0 16 16" aria-hidden="true"><path fill="#1b7a3a" d="M3.6 1.5l2.3 2.6-1.3 1.6c.8 1.9 2.3 3.5 4.3 4.5l1.6-1.3 2.6 2.3-1.4 2.3C7.2 13 3 8.8 1.6 3z"/></svg>
        0418693142
      </li>
      <li>
        <svg viewBox="0 0 16 16" aria-hidden="true"><rect x="1" y="3" width="14" height="10" fill="#1b7a3a"/><path d="M1.5 3.5L8 9l6.5-5.5" fill="none" stroke="#fff" stroke-width="1.2"/></svg>
        Miriam@KettleLedger-example.com.au
      </li>
      <li>
        <svg viewBox="0 0 16 16" aria-hidden="true"><circle cx="8" cy="8" r="6.5" fill="none" stroke="#1b7a3a" stroke-width="1.4"/><path d="M1.5 8h13M8 1.5c-3 3.5-3 9.5 0 13M8 1.5c3 3.5 3 9.5 0 13" fill="none" stroke="#1b7a3a" stroke-width="1"/></svg>
        www.kettleledger-example.com.au
      </li>
    </ul>

    <div class="services">Accounting | Payroll | Tax | SMSF | Technology</div>
    <div class="services-rule"></div>

    <div class="footer-band">
      <span class="band-green"></span>
      <span class="band-blue"></span>
    </div>
  </section>

</body>
</html>
```